Halvorn spray foam and Environmental

I have business cards but need new ones. The ones I have are very bland. Here is. Y company website http://www.halvornsprayfoam.ca

Also I can send you copies of the current cards
I would also need my current logo on the new design as well.. Also spray foam and Environmental

Industry/Entity Type

Business

Logo Text

Halvorn.

```html
<!DOCTYPE html>
<html lang="en">
<head>
<meta charset="utf-8">
<title>Halvorn Spray Foam – Business Card</title>
<link href="https://fonts.googleapis.com/css2?family=Montserrat:wght@700&family=Questrial&display=swap" rel="stylesheet">
<style>
  :root{
    --purple:#522068;
    --slate:#474d55;
    --silver:#b9bbbc;
    --ink:#1d1d1f;
    --muted:#6b6b70;
    --paper:#ffffff;
    --backdrop:#ebe8e4;
  }
  html,body{margin:0;padding:0;overflow:hidden;}
  body{width:1200px;height:953px;background:var(--backdrop);position:relative;font-family:"Questrial",sans-serif;}
  .card{position:absolute;top:322px;width:540px;height:309px;background:var(--paper);box-shadow:0 6px 18px rgba(0,0,0,.18);overflow:hidden;}
  .card--front{left:40px;}
  .card--back{left:620px;}
  .card__panel{position:absolute;left:0;top:0;width:270px;height:309px;background:linear-gradient(160deg,var(--purple) 0%,var(--purple) 62%,#5a4266 82%,var(--slate) 100%);}
  .services{position:absolute;left:26px;color:#fff;}
  .services--foam{top:44px;}
  .services--enviro{top:122px;}
  .services__title{font-family:"Montserrat",sans-serif;font-weight:700;font-size:22px;letter-spacing:.5px;margin:0 0 6px;}
  .services__list{margin:0;padding:0;list-style:none;font-size:9px;line-height:14px;}
  .brand{position:absolute;display:flex;align-items:center;gap:10px;}
  .brand__mark{width:34px;height:34px;background:var(--purple);flex:none;}
  .brand__name{font-family:"Montserrat",sans-serif;font-weight:700;font-size:24px;color:var(--purple);line-height:1;}
  .brand__tagline{font-family:"Questrial",sans-serif;font-size:12px;color:var(--muted);margin-top:4px;}
  .card--front .brand{left:318px;top:120px;}
  .card--back .brand{left:160px;top:62px;}
  .contact{position:absolute;top:170px;}
  .contact--foam{left:40px;}
  .contact--enviro{left:300px;}
  .contact__title{font-family:"Montserrat",sans-serif;font-weight:700;font-size:15px;color:var(--purple);margin:0 0 8px;}
  .contact__row{display:flex;align-items:center;gap:7px;font-size:11px;color:var(--ink);line-height:18px;}
  .icon{width:11px;height:11px;flex:none;}
  .address{position:absolute;left:40px;bottom:22px;display:flex;align-items:center;gap:7px;font-size:11px;color:var(--ink);}
</style>
</head>
<body>

<section class="card card--front">
  <div class="card__panel" role="img" aria-label="Decorative sweeping curve in purple, slate and silver"></div>

  <div class="services services--foam">
    <h2 class="services__title">SPRAY FOAM</h2>
    <ul class="services__list">
      <li>• Roofing Foam &nbsp;• Slabjacking &nbsp;• 2 Pound/Half Pound</li>
      <li>• Batt Insulation &nbsp;• Attic Blow In</li>
    </ul>
  </div>
  <div class="services services--enviro">
    <h2 class="services__title">ENVIROMENTAL</h2>
    <ul class="services__list">
      <li>• Air Monitoring &nbsp;• Asbestos Testing &nbsp;• Asbestos Removal</li>
      <li>• Building Demolition &nbsp;• Lead Testing &nbsp;• Mould Removal</li>
    </ul>
  </div>

  <div class="brand">
    <span class="brand__mark"></span>
    <div>
      <div class="brand__name">Halvorn</div>
      <div class="brand__tagline">Residential &amp; Commercial</div>
    </div>
  </div>
</section>

<section class="card card--back">
  <div class="brand">
    <span class="brand__mark"></span>
    <div>
      <div class="brand__name">Halvorn</div>
      <div class="brand__tagline">Residential &amp; Commercial</div>
    </div>
  </div>

  <div class="contact contact--foam">
    <h3 class="contact__title">SPRAY FOAM</h3>
    <div class="contact__row">
      <svg class="icon" viewBox="0 0 12 12"><path d="M3 1 L5 3.5 L4 4.8 C5 6.6 5.6 7.2 7.2 8 L8.5 7 L11 9 L9.6 11 C5 10.5 1.5 7 1 2.4 Z" fill="var(--purple)"/></svg>
      <span>604-555-0148</span>
    </div>
    <div class="contact__row">
      <svg class="icon" viewBox="0 0 12 12"><rect x="0.5" y="2" width="11" height="8" fill="var(--purple)"/><path d="M0.5 2 L6 6.5 L11.5 2" fill="none" stroke="#fff" stroke-width="1"/></svg>
      <span>halvornfoam@mailbox.ca</span>
    </div>
    <div class="contact__row">
      <svg class="icon" viewBox="0 0 12 12"><circle cx="6" cy="6" r="5.2" fill="var(--purple)"/><path d="M0.8 6 H11.2 M6 0.8 C3.5 3.5 3.5 8.5 6 11.2 M6 0.8 C8.5 3.5 8.5 8.5 6 11.2" fill="none" stroke="#fff" stroke-width=".8"/></svg>
      <span>www.halvornsprayfoam.ca</span>
    </div>
  </div>

  <div class="contact contact--enviro">
    <h3 class="contact__title">ENVIROMENTAL</h3>
    <div class="contact__row">
      <svg class="icon" viewBox="0 0 12 12"><path d="M3 1 L5 3.5 L4 4.8 C5 6.6 5.6 7.2 7.2 8 L8.5 7 L11 9 L9.6 11 C5 10.5 1.5 7 1 2.4 Z" fill="var(--purple)"/></svg>
      <span>604-555-0193</span>
    </div>
    <div class="contact__row">
      <svg class="icon" viewBox="0 0 12 12"><rect x="0.5" y="2" width="11" height="8" fill="var(--purple)"/><path d="M0.5 2 L6 6.5 L11.5 2" fill="none" stroke="#fff" stroke-width="1"/></svg>
      <span>halvornenviro@mailbox.ca</span>
    </div>
    <div class="contact__row">
      <svg class="icon" viewBox="0 0 12 12"><circle cx="6" cy="6" r="5.2" fill="var(--purple)"/><path d="M0.8 6 H11.2 M6 0.8 C3.5 3.5 3.5 8.5 6 11.2 M6 0.8 C8.5 3.5 8.5 8.5 6 11.2" fill="none" stroke="#fff" stroke-width=".8"/></svg>
      <span>www.halvornenvironmental.ca</span>
    </div>
  </div>

  <div class="address">
    <svg class="icon" viewBox="0 0 12 12"><path d="M6 0.5 C3.5 0.5 2 2.3 2 4.4 C2 7.2 6 11.5 6 11.5 C6 11.5 10 7.2 10 4.4 C10 2.3 8.5 0.5 6 0.5 Z" fill="var(--purple)"/><circle cx="6" cy="4.4" r="1.5" fill="#fff"/></svg>
    <span>4820 Larchmont Way Burnaby, British Columbia V5e 2k4, CA.</span>
  </div>
</section>

</body>
</html>
```